Webbanner-Design für Online Pfandhaus
Zielgruppe
Online Pfandhaus
Aufgabenstellung
Der Banner für unsere Webseite soll neu gestaltet werden. (Siehe Bilddatei)
Ziel ist es einen schönen, konvertierenden Banner zu gestalten. Der Banner soll sich an die Seite anpassen.
Der Banner wird dann auch für Social Media benötigt.

```html
<!DOCTYPE html>
<html lang="de">
<head>
<meta charset="utf-8">
<title>leihkiste.de – Ihr Online-Pfandhaus</title>
<link rel="stylesheet" href="https://fonts.googleapis.com/css2?family=Oswald:wght@500&family=Ubuntu:wght@700&family=Fira+Sans:wght@400&family=Open+Sans:wght@600;700&display=swap">
<style>
:root{
  --brand:#2b3d96;
  --band:#2a3c97;
  --hero-bg:#ebebeb;
  --ink:#111;
  --muted:#555a60;
  --heading:#4a4f55;
  --teal:#2b9ea0;
  --chat:#27c23d;
  --white:#fff;
}
*{margin:0;padding:0;box-sizing:border-box}
html,body{width:1200px;height:889px;overflow:hidden;background:var(--white)}
.page{position:relative;width:1200px;height:889px;overflow:hidden;font-family:"Fira Sans",sans-serif;color:var(--ink)}
.site-header{position:absolute;top:0;left:0;width:1200px;height:74px;background:var(--white)}
.brand{position:absolute;left:70px;top:20px;display:flex;align-items:center;gap:8px;font-family:"Ubuntu",sans-serif;font-weight:700;font-size:21px;color:var(--brand)}
.brand-dot{width:34px;height:34px;border-radius:50%;background:var(--brand)}
.main-nav{position:absolute;top:24px;left:0;width:1200px;font-family:"Oswald",sans-serif;font-weight:500;font-size:19px;color:var(--brand)}
.main-nav span{position:absolute;white-space:nowrap}
.hero{position:absolute;top:74px;left:0;width:1200px;height:550px}
.hero-copy{position:absolute;left:0;top:0;width:643px;text-align:center}
.hero-title{position:absolute;top:58px;width:643px;font-family:"Ubuntu",sans-serif;font-weight:700;font-size:64px;color:var(--brand);letter-spacing:.5px}
.hero-sub{position:absolute;top:130px;width:643px;font-size:41px;color:var(--ink)}
.hero-lead{position:absolute;top:182px;width:643px;font-size:21px;line-height:33px}
.hero-question{position:absolute;top:268px;width:643px;font-size:15px}
.loan-form{position:absolute;top:296px;left:201px;display:flex;gap:11px}
.loan-select{width:137px;height:42px;background:var(--white);border-radius:3px;display:flex;align-items:center;justify-content:space-between;padding:0 9px 0 12px;font-size:15px}
.loan-button{width:89px;height:42px;background:var(--teal);color:var(--white);border-radius:3px;display:flex;align-items:center;justify-content:center;font-size:15px}
.hero-alt{position:absolute;top:353px;width:643px;font-size:15px}
.hero-alt b{color:var(--chat);font-weight:400}
.member{position:absolute;top:392px;left:180px;display:flex;align-items:center;gap:18px;font-size:11px;text-align:right;line-height:14px}
.member-badge{width:44px;height:50px;background:#d52b2b;border-radius:4px}
.hero-visual{position:absolute;left:673px;top:46px;width:495px;height:461px;border-radius:8px;background:linear-gradient(160deg,#3a3a3a 0%,#8fa6c2 30%,#c4703e 55%,#d2a947 80%,#e7e7e7 100%)}
.band{position:absolute;left:0;top:530px}
.chat-button{position:absolute;left:1123px;top:607px;width:48px;height:48px;border-radius:50%;background:var(--chat);display:flex;align-items:center;justify-content:center}
.features{position:absolute;top:646px;left:0;width:1200px}
.feature{position:absolute;width:170px;margin-left:-85px;text-align:center;font-family:"Open Sans",sans-serif;font-weight:600;font-size:18px;line-height:25px;color:var(--muted)}
.feature svg{display:block;margin:0 auto 8px}
.steps-title{position:absolute;top:770px;width:1200px;text-align:center;font-family:"Open Sans",sans-serif;font-weight:700;font-size:38px;color:var(--heading)}
.step{position:absolute;top:842px;width:70px;height:70px;margin-left:-35px;border:5px solid var(--teal);border-radius:50%;text-align:center;font-family:"Open Sans",sans-serif;font-weight:600;font-size:38px;line-height:64px;color:var(--teal)}
</style>
</head>
<body>
<div class="page">
  <header class="site-header">
    <div class="brand"><span class="brand-dot"></span>leihKiste.de</div>
    <nav class="main-nav">
      <span style="left:408px">Start</span>
      <span style="left:478px">Anfrage</span>
      <span style="left:567px">Ablauf</span>
      <span style="left:646px">Wissenswertes</span>
      <span style="left:781px">FAQ</span>
      <span style="left:842px">Standorte <svg width="12" height="8" viewBox="0 0 12 8"><path d="M1 1l5 5 5-5" fill="none" stroke="currentColor" stroke-width="2"/></svg></span>
      <span style="left:964px">Kontakt</span>
      <span style="left:1054px">Über uns</span>
    </nav>
  </header>

  <section class="hero">
    <svg class="band" width="1200" height="95" viewBox="0 0 1200 95" style="top:-74px;position:absolute">
    </svg>
    <svg style="position:absolute;left:0;top:0" width="1200" height="550" viewBox="0 0 1200 550">
      <path d="M0 0H1200V464L600 521L0 464Z" fill="var(--hero-bg)"/>
      <path d="M0 464L600 521L1200 464V490L600 545L0 490Z" fill="var(--band)"/>
    </svg>
    <div class="hero-copy">
      <h1 class="hero-title">leihkiste.de</h1>
      <p class="hero-sub">Ihr Online-Pfandhaus</p>
      <p class="hero-lead">Bei uns erhalten Sie in kürzester Zeit Geld fur<br>Ihre Wertgegenstände.</p>
      <p class="hero-question">Weichen Wertgegenstand möchten Sie belehen?</p>
      <div class="loan-form">
        <div class="loan-select">Schmuck <svg width="13" height="8" viewBox="0 0 13 8"><path d="M1 1l5.5 5.5L12 1" fill="none" stroke="#666" stroke-width="1.3"/></svg></div>
        <div class="loan-button">Anfrage</div>
      </div>
      <p class="hero-alt">Alternative können Sie uns auch direkt unter <b>ChatDirekt</b> kontraktien.</p>
      <div class="member">
        <p>Wir sind Mitglied im Bundesverband<br>der Leihhäuser e.V.</p>
        <div class="member-badge"></div>
      </div>
    </div>
    <div class="hero-visual" role="img" aria-label="Monitor, Laptop und Smartphone mit Goldbarren, Ringen, Edelstein und Armbanduhren"></div>
  </section>

  <div class="chat-button">
    <svg width="24" height="24" viewBox="0 0 24 24"><path d="M6 3l4 1 1 4-2 2c1 2.5 3 4.5 5 5l2-2 4 1 1 4-2 2C10 20 4 14 4 5z" fill="var(--white)"/></svg>
  </div>

  <section class="features">
    <div class="feature" style="left:177px">
      <svg width="40" height="28" viewBox="0 0 40 28"><rect x="2" y="3" width="36" height="22" rx="2" fill="none" stroke="var(--brand)" stroke-width="4"/><circle cx="20" cy="14" r="6" fill="var(--brand)"/></svg>schnelle<br>Auszahlung</div>
    <div class="feature" style="left:346px">
      <svg width="40" height="28" viewBox="0 0 40 28"><path d="M2 5l10-4 8 5 8-5 10 4-4 6v14H6V11z" fill="var(--brand)"/></svg>versichert bis<br>5000 €</div>
    <div class="feature" style="left:515px">
      <svg width="32" height="32" viewBox="0 0 32 32" style="margin-top:-4px;margin-bottom:8px"><circle cx="16" cy="16" r="13.5" fill="none" stroke="var(--brand)" stroke-width="3"/><path d="M10 16l4 4 8-8" fill="none" stroke="var(--brand)" stroke-width="3"/></svg>keine<br>Bonitätsprüfung</div>
    <div class="feature" style="left:683px">
      <svg width="38" height="30" viewBox="0 0 38 30" style="margin-top:-2px"><path d="M19 1L1 16h5v13h9v-9h8v9h9V16h5z" fill="var(--brand)"/></svg>Abholung von<br>Zuhause</div>
    <div class="feature" style="left:852px">
      <svg width="40" height="30" viewBox="0 0 40 30" style="margin-top:-2px"><path d="M2 20l10-8h10l-4 6h8l10-12v10L26 28H6z" fill="var(--brand)"/></svg>100% Diskretion</div>
    <div class="feature" style="left:1021px">
      <svg width="32" height="32" viewBox="0 0 32 32" style="margin-top:-4px;margin-bottom:8px"><circle cx="16" cy="16" r="15" fill="var(--brand)"/><circle cx="11" cy="12" r="2" fill="#fff"/><circle cx="21" cy="12" r="2" fill="#fff"/><path d="M9 19q7 7 14 0" fill="none" stroke="#fff" stroke-width="2.5"/></svg>Faire Bewertung</div>
  </section>

  <h2 class="steps-title">So funktioniert's:</h2>
  <div class="step" style="left:273px">1</div>
  <div class="step" style="left:600px">2</div>
  <div class="step" style="left:927px">3</div>
</div>
</body>
</html>
```